Hosted Phone Service

We provide hosted phone service for less than $19.00 per user/seat. For many offices this is less money than what they are paying for their traditional phone lines.

Industry/Entity Type

Phone Service

```html
<!DOCTYPE html>
<html lang="en">
<head>
<meta charset="utf-8">
<title>Hosted Phone Service Postcard</title>
<link rel="stylesheet" href="https://fonts.googleapis.com/css2?family=Tinos:wght@700&family=Open+Sans:wght@400;600;700&display=swap">
<style>
  :root {
    --page-bg: #d9dadc;
    --navy: #1f3a8f;
    --navy-deep: #1c2f7a;
    --sky: #1a9fe0;
    --ocean: #0b5fb3;
    --pale: #e4f1fb;
    --photo-light: #dfeefa;
    --photo-mid: #9cc8ea;
    --white: #ffffff;
    --ink-line: #3a3a3a;
    --divider: #8b8f96;
  }
  * { box-sizing: border-box; margin: 0; padding: 0; }
  html, body { width: 1200px; height: 1200px; overflow: hidden; }
  body {
    background: var(--page-bg);
    display: flex;
    flex-direction: column;
    align-items: center;
    justify-content: center;
    gap: 30px;
  }
  .postcard {
    position: relative;
    width: 840px;
    height: 560px;
    overflow: hidden;
    background: var(--white);
    box-shadow: 0 4px 14px rgba(0,0,0,0.18);
  }
  .postcard-front svg { position: absolute; inset: 0; }
  .front-logo {
    position: absolute;
    right: 40px;
    top: 168px;
    display: flex;
    align-items: center;
    gap: 12px;
    font-family: "Tinos", serif;
    font-weight: 700;
    font-size: 34px;
    color: var(--navy);
  }
  .front-logo .logo-dot {
    width: 26px;
    height: 26px;
    border-radius: 50%;
    background: var(--navy);
  }
  .front-headline {
    position: absolute;
    left: 240px;
    right: 16px;
    top: 410px;
    text-align: center;
    font-family: "Tinos", serif;
    font-weight: 700;
    font-size: 38px;
    line-height: 1.12;
    letter-spacing: 0.5px;
    color: var(--navy-deep);
    text-transform: uppercase;
  }
  .postcard-back { display: flex; }
  .back-features {
    width: 47%;
    height: 100%;
    background: linear-gradient(180deg, var(--sky) 0%, #128bd4 40%, var(--ocean) 100%);
    padding: 30px 22px 0 34px;
    border-right: 3px solid var(--divider);
  }
  .feature-list { list-style: none; }
  .feature-list li {
    position: relative;
    padding-left: 22px;
    font-family: "Open Sans", sans-serif;
    font-weight: 600;
    font-size: 15px;
    line-height: 1.45;
    color: var(--white);
  }
  .feature-list li::before {
    content: "";
    position: absolute;
    left: 2px;
    top: 6px;
    border-left: 9px solid var(--white);
    border-top: 5px solid transparent;
    border-bottom: 5px solid transparent;
  }
  .feature-list .price {
    font-weight: 700;
    font-size: 21px;
  }
  .back-address {
    position: relative;
    flex: 1;
    background: var(--white);
  }
  .stamp-box {
    position: absolute;
    right: 44px;
    top: 44px;
    width: 96px;
    height: 80px;
    border: 2px solid var(--ink-line);
  }
  .address-lines {
    position: absolute;
    left: 40px;
    right: 40px;
    top: 190px;
    display: flex;
    flex-direction: column;
    gap: 44px;
  }
  .address-lines span {
    display: block;
    height: 0;
    border-top: 2px solid var(--ink-line);
  }
</style>
</head>
<body>

  <section class="postcard postcard-front">
    <svg width="840" height="560" viewBox="0 0 840 560">
      <defs>
        <linearGradient id="photoTone" x1="0" y1="0" x2="1" y2="1">
          <stop offset="0" stop-color="var(--photo-mid)"/>
          <stop offset="0.55" stop-color="var(--photo-light)"/>
          <stop offset="1" stop-color="#f4f8fc"/>
        </linearGradient>
      </defs>
      <rect class="front-base" width="840" height="560" fill="var(--pale)"/>
      <path class="front-corner" d="M0,0 H120 C110,70 80,120 0,150 Z" fill="var(--white)"/>
      <path class="front-photo" role="img" aria-label="Photo of hands typing on a laptop with a glowing world map and floating media screens"
            d="M120,0 H840 V250 C700,310 480,320 320,272 C190,232 108,130 120,0 Z" fill="url(#photoTone)"/>
      <path class="front-photo-edge" d="M120,0 C108,130 190,232 320,272 C480,320 700,310 840,250" fill="none" stroke="var(--sky)" stroke-width="7"/>
      <path class="front-sweep" d="M0,150 C60,260 180,322 340,345 C520,370 700,340 840,285 V312 C700,365 520,385 380,380 C250,376 120,420 60,560 H0 Z" fill="var(--navy)"/>
      <path class="front-sweep-edge" d="M0,150 C60,260 180,322 340,345 C520,370 700,340 840,285" fill="none" stroke="var(--sky)" stroke-width="4"/>
    </svg>
    <div class="front-logo"><span class="logo-dot"></span>Linewise Voice</div>
    <h1 class="front-headline">Save money with hosted<br>phone service</h1>
  </section>

  <section class="postcard postcard-back">
    <div class="back-features">
      <ul class="feature-list">
        <li>No long term contract or cancellation fees</li>
        <li>Keep your existing numbers</li>
        <li>Top of the line phone service</li>
        <li>Lifetime customer support</li>
        <li>Unlimited local and long distance</li>
        <li>Standard Features Included</li>
        <li>Customizable: Pay for only what you need add and subtract phones as your company changes</li>
        <li>One phone system for single or multiple locations</li>
        <li>As low as <span class="price">$19.00</span> per user.</li>
      </ul>
    </div>
    <div class="back-address">
      <div class="stamp-box"></div>
      <div class="address-lines">
        <span></span><span></span><span></span><span></span><span></span>
      </div>
    </div>
  </section>

</body>
</html>
```